Dental Business Card

I need Dental oriented business cards.
On the front side -
- on the first line, my name:
Dr Marlo Vintner
- on the second line (just underneath):
Doctor of Dental Medicine
- on the third line, or underneath that or in a corner, I would like the address and phone number:
5182 Ch. Birchfield
Montreal QC H2T 4B9
514-629-5074
- other than that i would maybe like a logo of a tooth, but i want it to be subtle and very basic!
- I would like the card to be preferably black or dark grey-ish with the writing in white
On the other side -
- 2-3 lines with the possibility to write the next appointment the box with the lines should be white, with the rest of the card being black

```html
<!DOCTYPE html>
<html lang="en">
<head>
<meta charset="utf-8">
<title>Dr Marlo Vintner – Business Card</title>
<link rel="stylesheet" href="https://fonts.googleapis.com/css2?family=Archivo:wdth,wght@62..125,300..700&display=swap">
<style>
  :root {
    --card-black: #000000;
    --ink-white: #f2f2f2;
    --mark-grey: #1c1c1c;
  }
  html, body {
    margin: 0;
    padding: 0;
    width: 1200px;
    height: 686px;
    overflow: hidden;
    background: var(--card-black);
  }
  .card {
    position: relative;
    width: 1200px;
    height: 686px;
    background: var(--card-black);
    font-family: "Archivo", "Helvetica Neue", Arial, sans-serif;
    color: var(--ink-white);
  }
  .tooth-mark {
    position: absolute;
    left: 743px;
    top: 74px;
    width: 434px;
    height: 566px;
    border-radius: 48% 48% 40% 40% / 30% 30% 60% 60%;
    background: radial-gradient(ellipse at 50% 40%, var(--mark-grey) 0%, rgba(28,28,28,0.5) 55%, rgba(0,0,0,0) 75%);
  }
  .identity {
    position: absolute;
    left: 85px;
    top: 224px;
  }
  .doctor-name {
    margin: 0;
    font-size: 46px;
    font-weight: 700;
    font-stretch: 125%;
    letter-spacing: 0.1em;
    line-height: 1;
    text-transform: uppercase;
  }
  .doctor-title {
    margin: 10px 0 0;
    font-size: 31px;
    font-weight: 300;
    font-stretch: 90%;
    line-height: 1;
    text-transform: uppercase;
  }
  .contact {
    margin: 44px 0 0;
    font-style: normal;
    font-size: 31px;
    font-weight: 300;
    font-stretch: 90%;
    line-height: 39px;
    text-transform: uppercase;
  }
</style>
</head>
<body>
  <div class="card">
    <div class="tooth-mark" role="img" aria-label="Subtle faint tooth outline mark"></div>
    <div class="identity">
      <h1 class="doctor-name">Dr. Marlo Vintner</h1>
      <p class="doctor-title">Doctor of Dental Medicine</p>
      <address class="contact">
        5182 Ch. Birchfield<br>
        Montreal QC H2T 4B9<br>
        514-629-5074
      </address>
    </div>
  </div>
</body>
</html>
```